Enterprise software provider needs a product brochure

We need an A5 portrait product brochure (8 pages) to tell people about our compliance software for the oil and gas industry. We want to use the colours from our logo (see attached logo file) and imagery that reflects the oil and gas sector and legal/professional services.See attached documents for details.

Target Market(s)

oil and gas, lawyers, compliance professionals

Colors

```html
<!DOCTYPE html>
<html lang="en">
<head>
<meta charset="utf-8">
<title>Regulyx Brochure Spreads</title>
<link href="https://fonts.googleapis.com/css2?family=Montserrat:wght@400;500;600&family=PT+Sans+Narrow&family=Titillium+Web:ital,wght@1,700&display=swap" rel="stylesheet">
<style>
  :root{
    --bg:#d9d9d9;
    --bg-deep:#b9b9b9;
    --blue-dark:#1679b0;
    --blue:#1f9ad3;
    --blue-light:#39b4e6;
    --sky:#6ccbf0;
    --green:#a9d24a;
    --green-light:#d4ea84;
    --teal:#7fd0c4;
    --text:#1d1d1d;
    --white:#ffffff;
  }
  *{margin:0;padding:0;box-sizing:border-box}
  html,body{width:1010px;height:1200px;overflow:hidden}
  body{
    position:relative;
    background:linear-gradient(180deg,var(--bg) 0%,var(--bg-deep) 60%,var(--bg) 100%);
    font-family:"Montserrat",sans-serif;
  }
  .page{position:absolute;width:433px;height:560px;background:var(--white);overflow:hidden}
  .page--back{left:71px;top:34px}
  .page--front{left:529px;top:34px}
  .page--difference{left:71px;top:617px}
  .page--intelligence{left:529px;top:617px}
  .page svg.art{position:absolute;left:0;top:0;width:433px;height:560px}

  /* back cover */
  .back-name{position:absolute;left:0;width:340px;top:191px;text-align:center;color:var(--white);font-size:28px;font-weight:400;letter-spacing:.3px}
  .contact-box{position:absolute;left:14px;top:226px;width:209px;height:112px;border:1px solid var(--white);padding:14px 0 0 17px}
  .contact-box p{color:var(--white);font-size:12px;line-height:13.8px;letter-spacing:.3px}
  .contact-icon{position:absolute;left:200px;width:14px;height:14px;background:var(--blue)}
  .contact-icon svg{display:block;width:14px;height:14px}

  /* front cover */
  .front-name{position:absolute;left:68px;top:11px;color:var(--blue-dark);font-size:41px;font-weight:500;letter-spacing:.2px}
  .front-tagline{position:absolute;left:61px;top:55px;color:var(--blue-dark);font-size:12.5px;font-weight:500;letter-spacing:.3px}
  .front-band{position:absolute;left:0;top:92px;width:433px;height:47px;background:linear-gradient(90deg,rgba(255,255,255,0) 0%,#f2f8f6 100%)}
  .front-claim{position:absolute;right:11px;top:100px;text-align:right;font-size:13.5px;font-weight:500;line-height:16px;letter-spacing:.2px;
    background:linear-gradient(90deg,var(--green) 0%,var(--teal) 60%,var(--blue) 100%);-webkit-background-clip:text;background-clip:text;color:transparent}

  /* inner pages */
  .photo{position:absolute;left:0;top:0;width:433px;height:148px}
  .photo--dawn{background:linear-gradient(180deg,#9fb7b2 0%,#d7d5c3 40%,#f0caa3 70%,#6f8189 74%,#4e6169 100%)}
  .photo--sunset{background:linear-gradient(180deg,#e9e4d6 0%,#f0dcbc 35%,#f7c98a 62%,#7d7a70 70%,#5c6568 100%)}
  .wave{position:absolute;left:0;top:0;width:433px;height:175px}
  .inner-name{position:absolute;left:18px;top:58px;color:var(--white);font-size:16.5px;font-weight:400;letter-spacing:.3px}
  .section-title{position:absolute;left:117px;top:70px;color:var(--white);font-family:"Titillium Web",sans-serif;font-style:italic;font-weight:700;font-size:37px;letter-spacing:.5px;text-decoration:underline;text-decoration-thickness:2px;text-underline-offset:3px}
  .body-copy{position:absolute;top:229px;width:342px;font-family:"PT Sans Narrow",sans-serif;font-size:9.2px;line-height:11.2px;color:var(--text);text-align:justify}
  .body-copy p+p{margin-top:11px}
  .page--difference .body-copy{left:40px}
  .page--intelligence .body-copy{left:47px;width:337px}
  .accent-bar{position:absolute;left:21px;top:229px;width:3px;height:95px;background:linear-gradient(180deg,var(--green-light),var(--sky))}
  .page--intelligence .accent-bar{left:23px;height:56px}
  .headline{position:absolute;top:344px;font-size:23.5px;font-weight:500;line-height:29px;letter-spacing:.4px;
    background:linear-gradient(90deg,var(--sky) 0%,var(--teal) 50%,var(--green) 100%);-webkit-background-clip:text;background-clip:text;color:transparent}
  .page--difference .headline{right:27px;text-align:right}
  .page--intelligence .headline{left:0;width:433px;text-align:center}
  .quote{position:absolute;top:413px;width:261px;height:112px;padding:29px 16px 0 17px;color:var(--white)}
  .page--difference .quote{left:96px;border-radius:30px 0 30px 0;background:linear-gradient(90deg,var(--sky) 0%,var(--teal) 55%,var(--green) 100%)}
  .page--intelligence .quote{left:79px;border-radius:0 30px 0 30px;background:linear-gradient(90deg,var(--green) 0%,var(--teal) 55%,var(--sky) 100%)}
  .quote p{font-size:8.9px;line-height:11.2px;text-align:justify;font-weight:500}
  .quote cite{display:block;text-align:right;font-style:normal;font-size:8.9px;font-weight:500;margin-top:11px}
  .foot-strip{position:absolute;left:0;top:547px;width:433px;height:13px}
  .page--difference .foot-strip{background:linear-gradient(90deg,var(--sky),var(--teal),var(--green))}
  .page--intelligence .foot-strip{background:linear-gradient(90deg,var(--teal),var(--green))}
</style>
</head>
<body>

<!-- Back cover -->
<section class="page page--back">
  <svg class="art" viewBox="0 0 733 947" preserveAspectRatio="none" aria-hidden="true">
    <defs>
      <linearGradient id="backBlue" x1="0" y1="0" x2="1" y2="0">
        <stop offset="0" stop-color="#1679b0"/><stop offset="1" stop-color="#24a6dd"/>
      </linearGradient>
      <linearGradient id="backGreen" x1="0" y1="1" x2="1" y2="0">
        <stop offset="0" stop-color="#a9d24a"/><stop offset="1" stop-color="#d4ea84"/>
      </linearGradient>
    </defs>
    <path d="M0,0 L330,0 C450,90 580,150 733,220 L733,365 C450,520 250,760 155,947 L0,947 Z" fill="url(#backBlue)"/>
    <path d="M270,947 C400,750 560,570 733,480 L733,620 C660,720 620,830 605,947 Z" fill="url(#backGreen)"/>
  </svg>
  <div class="back-name">Regulyx</div>
  <div class="contact-box">
    <p>Level 4, 88 Harbour Street</p>
    <p>Easton 4120</p>
    <p>New Zealand</p>
    <p>+64-4-555-0182</p>
    <p>sales@regulyx.com</p>
    <p>www.regulyx.com</p>
    <span class="contact-icon" style="top:14px"><svg viewBox="0 0 14 14"><path d="M7 1a4 4 0 0 1 4 4c0 3-4 8-4 8S3 8 3 5a4 4 0 0 1 4-4z" fill="#fff"/><circle cx="7" cy="5" r="1.5" fill="#1f9ad3"/></svg></span>
    <span class="contact-icon" style="top:38px"><svg viewBox="0 0 14 14"><path d="M3 1.5l2.5 0 1 3-1.5 1.2a7 7 0 0 0 3.3 3.3L9.5 7.5l3 1v2.5c0 .8-.7 1.5-1.5 1.5A10 10 0 0 1 1.5 3c0-.8.7-1.5 1.5-1.5z" fill="#fff"/></svg></span>
    <span class="contact-icon" style="top:61px"><svg viewBox="0 0 14 14"><rect x="1" y="3" width="12" height="8" fill="#fff"/><path d="M1 3l6 5 6-5" fill="none" stroke="#1f9ad3" stroke-width="1"/></svg></span>
    <span class="contact-icon" style="top:84px"><svg viewBox="0 0 14 14"><circle cx="7" cy="7" r="6" fill="#fff"/><g fill="none" stroke="#1f9ad3" stroke-width=".9"><ellipse cx="7" cy="7" rx="2.6" ry="6"/><path d="M1 7h12M2 4h10M2 10h10"/></g></svg></span>
  </div>
</section>

<!-- Front cover -->
<section class="page page--front">
  <svg class="art" viewBox="0 0 733 947" preserveAspectRatio="none">
    <defs>
      <linearGradient id="frontBlue" x1="0" y1="0" x2="1" y2="0">
        <stop offset="0" stop-color="#1f9ad3"/><stop offset="1" stop-color="#3ab8e8"/>
      </linearGradient>
      <linearGradient id="frontGreen" x1="0" y1="1" x2="1" y2="0">
        <stop offset="0" stop-color="#c3e06c"/><stop offset="1" stop-color="#dcee95"/>
      </linearGradient>
      <linearGradient id="rigScene" x1="0" y1="0" x2="0" y2="1">
        <stop offset="0" stop-color="#d3e0ea"/><stop offset=".45" stop-color="#9fb3c2"/>
        <stop offset=".75" stop-color="#8a97a2"/><stop offset=".85" stop-color="#b8c6d0"/>
        <stop offset="1" stop-color="#7d8f9c"/>
      </linearGradient>
    </defs>
    <path d="M0,221 C90,230 160,245 220,261 C160,290 80,330 0,365 Z" fill="url(#frontBlue)"/>
    <path d="M0,600 C60,520 150,420 265,341 C170,430 90,530 0,690 Z" fill="url(#frontGreen)"/>
    <g role="img" aria-label="Offshore jack-up drilling rig at sea under a bright cloudy sky">
      <path d="M40,947 C90,620 380,330 733,268 L733,947 Z" fill="url(#rigScene)"/>
    </g>
  </svg>
  <div class="front-name">Regulyx</div>
  <div class="front-tagline">THE OIL AND GAS COMPLIANCE TOOL</div>
  <div class="front-band"></div>
  <div class="front-claim">THE CLOUD SOLUTION FOR COMPLIANCE AND RISK<br>IN THE OIL AND GAS INDUSTRY</div>
</section>

<!-- Inner page: our difference -->
<section class="page page--difference">
  <div class="photo photo--dawn" role="img" aria-label="Calm sea horizon at dawn with soft pastel sky"></div>
  <svg class="wave" viewBox="0 0 733 296" preserveAspectRatio="none" aria-hidden="true">
    <defs>
      <linearGradient id="waveCool" x1="0" y1="0" x2="1" y2="0">
        <stop offset="0" stop-color="#8fd6ec"/><stop offset="1" stop-color="#b7e3c6"/>
      </linearGradient>
      <radialGradient id="hazeCool" cx=".5" cy=".6" r=".6">
        <stop offset="0" stop-color="#eaf5fb"/><stop offset="1" stop-color="#ffffff" stop-opacity="0"/>
      </radialGradient>
    </defs>
    <path d="M0,230 C250,250 500,260 733,251 L733,281 C500,280 250,265 0,230 Z" fill="url(#waveCool)"/>
    <path d="M0,251 L733,251 L733,296 L0,296 Z" fill="url(#hazeCool)" opacity=".4"/>
  </svg>
  <div class="inner-name">Regulyx</div>
  <h1 class="section-title">OUR DIFFERENCE</h1>
  <span class="accent-bar"></span>
  <div class="body-copy">
    <p>Managing an upstream oil and gas portfolio is complex, with regulatory and contractual obligations differing across locations and operations.</p>
    <p>Developed by industry experts, Regulyx has been designed specifically to address the unique challenges faced by oil and gas operators. Bringing together your licence information and commitments with the regulatory, contractual and internal process requirements and risks associated with your operations, Regulyx gives you a holistic view of your E&amp;P assets and activities.</p>
  </div>
  <h2 class="headline">WE UNDERSTAND YOUR<br>BUSINESS.</h2>
  <blockquote class="quote">
    <p>“The activity planning and look ahead we get from Regulyx means we are able to be pro-active but also respond and adapt more quickly when things do change.”</p>
    <cite>- HSE, Risk and Compliance Manager</cite>
  </blockquote>
  <div class="foot-strip"></div>
</section>

<!-- Inner page: compliance intelligence -->
<section class="page page--intelligence">
  <div class="photo photo--sunset" role="img" aria-label="Offshore rig silhouetted against a setting sun over the sea"></div>
  <svg class="wave" viewBox="0 0 733 296" preserveAspectRatio="none" aria-hidden="true">
    <defs>
      <linearGradient id="waveWarm" x1="0" y1="0" x2="1" y2="0">
        <stop offset="0" stop-color="#b7e3c6"/><stop offset="1" stop-color="#c6e28a"/>
      </linearGradient>
    </defs>
    <path d="M0,251 C250,262 500,262 733,230 L733,240 C500,285 250,285 0,281 Z" fill="url(#waveWarm)"/>
  </svg>
  <span class="accent-bar"></span>
  <div class="body-copy">
    <p>Regulyx has in-built compliance intelligence, empowering your operational teams to confidently manage compliance in the context of their day-to-day activities.</p>
    <p>Our unique data architecture delivers compliance information to the people who need it, when they need it.</p>
  </div>
  <h2 class="headline">COMPLIANCE INTELLIGENCE</h2>
  <blockquote class="quote">
    <p>“Regulyx allows me as a manager to get status reports on every permit's compliance against regulatory deadlines. It has kept us out of trouble a number of times.”</p>
    <cite>- Exploration Manager</cite>
  </blockquote>
  <div class="foot-strip"></div>
</section>

</body>
</html>
```